Web design required

1-We need a web design for existing company based in New Zealand
2-We build residential house and light commercial
3-We has in-house designer which allow us can provide interior design
4-We modeling project before site construction, which enable both client and construction team to visually analysis whole project,

Target Market(s)

middle class residential house market
Ref: http://www.brambleworthbuilders.co.nz/

Industry/Entity Type

Construction Company

Number of Pages Required

1 page

Font styles to use
Sans Serif
Other font styles liked:
• Such as : Central Gothic or similar which has more design taste

Colors

Designer to choose colors to be used in the design.

Requirements
Must have
• Front sheet, contact information, sample project

```html
<!DOCTYPE html>
<html lang="en">
<head>
<meta charset="utf-8">
<title>Harbourline Homes</title>
<link href="https://fonts.googleapis.com/css2?family=Montserrat:wght@400;500;600;700&family=Questrial&display=swap" rel="stylesheet">
<style>
:root{
  --blue:#1a4f9c;
  --blue-dark:#123d7d;
  --ink:#2b2b2b;
  --text:#555;
  --muted:#8a8a8a;
  --grey-bg:#efefef;
  --line:#d8d8d8;
  --dark:#2f3338;
  --footer:#24282d;
  --white:#fff;
}
*{margin:0;padding:0;box-sizing:border-box}
html,body{width:1200px;height:3093px;overflow:hidden}
body{position:relative;background:var(--white);font-family:"Questrial",sans-serif;color:var(--text)}
.abs{position:absolute}
.heading{font-family:"Montserrat",sans-serif;font-weight:600;color:var(--ink);font-size:27px;letter-spacing:.5px}
.heading span{color:var(--blue)}
.center{left:0;width:1200px;text-align:center}
.divider{position:absolute;left:440px;width:320px;height:26px}
.btn{position:absolute;background:var(--blue);color:var(--white);font-family:"Montserrat",sans-serif;font-weight:600;font-size:11px;letter-spacing:.6px;display:flex;align-items:center;justify-content:center}

/* header */
.topbar{left:742px;top:0;width:320px;height:29px;background:var(--blue);color:var(--white);font-size:12px;display:flex;align-items:center;justify-content:center;gap:22px;clip-path:polygon(4% 0,100% 0,96% 100%,0 100%)}
.topbar-rule{left:0;top:0;width:1200px;height:3px;background:var(--blue)}
.brand{left:144px;top:24px;display:flex;align-items:center;gap:12px}
.brand-mark{width:44px;height:44px;background:var(--blue);border-radius:50%}
.brand-name{font-family:"Montserrat",sans-serif;font-weight:600;font-size:22px;color:var(--blue);letter-spacing:2px;line-height:1}
.nav{top:58px;font-family:"Montserrat",sans-serif;font-weight:500;font-size:12px;color:var(--ink)}
.nav.active{color:var(--blue)}
.nav-hex{left:514px;top:34px}

/* hero */
.hero{left:0;top:103px;width:1200px;height:481px;background:linear-gradient(180deg,#8fa1ae 0%,#9b8a74 35%,#7e8d5c 65%,#5f8a38 100%)}
.hero-band{left:0;top:526px;width:1200px;height:58px;background:rgba(30,34,38,.62);color:var(--white);font-family:"Montserrat",sans-serif;font-size:24px;font-weight:500;letter-spacing:.6px;display:flex;align-items:center;justify-content:center}
.hero-arrow{top:298px;width:44px;height:44px;border-radius:50%;background:rgba(255,255,255,.35)}

/* about */
.about-text{left:144px;top:720px;width:623px;font-size:12.5px;line-height:21.5px}
.estimate{left:798px;top:650px;width:262px;height:303px;border:1px solid var(--line);background:var(--white)}
.estimate-tab{left:798px;top:650px;width:262px;height:62px;background:var(--dark);clip-path:polygon(0 0,100% 0,100% 68%,50% 100%,0 68%);color:var(--white);font-family:"Montserrat",sans-serif;font-weight:600;font-size:16px;text-align:center;padding-top:12px}
.field{left:812px;width:233px;border:1px solid var(--line);font-size:10.5px;color:var(--muted);font-style:italic;padding:8px 10px}

/* services */
.services-bg{left:0;top:1014px;width:1200px;height:642px;background:var(--grey-bg)}
.card{top:1161px;width:437px;height:433px;background:var(--white);border-bottom:3px solid var(--blue)}
.card-img{position:absolute;left:6px;top:6px;width:425px;height:210px}
.card-title{position:absolute;top:272px;width:100%;text-align:center;font-family:"Montserrat",sans-serif;font-weight:600;font-size:19px;color:var(--ink)}
.card-text{position:absolute;left:50px;top:300px;width:337px;text-align:center;font-size:11.5px;line-height:17.5px}

/* testimonials */
.testi-bg{left:0;top:2305px;width:1200px;height:479px;background:var(--grey-bg)}
.avatar{top:2460px;width:90px;height:90px;border-radius:50%;border:3px solid #555;background:linear-gradient(160deg,#c9ad97,#8b6a57)}
.avatar.active{border-color:var(--blue)}
.person{top:2565px;width:160px;text-align:center;font-size:12px;color:var(--ink)}
.person.active{color:var(--blue)}
.quote{left:150px;top:2608px;width:900px;height:110px;background:var(--white);border:1px solid var(--line);font-size:12px;line-height:21px;text-align:center;padding:16px 60px}
.quote-mark{font-family:"Montserrat",sans-serif;font-size:40px;color:#dcdcdc;line-height:1}

/* footer */
.footer{left:0;top:2784px;width:1200px;height:309px;background:linear-gradient(180deg,#33383e 0%,#262a2f 60%,#1c1f23 100%)}
.foot-head{top:2825px;font-family:"Montserrat",sans-serif;font-weight:600;font-size:12.5px;color:var(--white);letter-spacing:.5px}
.foot-links{left:150px;top:2862px;list-style:none;font-size:11.5px;color:#d6d6d6;line-height:23.2px}
.foot-links li::before{content:"»";color:#aaa;margin-right:10px}
.contact{left:355px;top:2862px;font-size:11.5px;color:#d6d6d6;line-height:17px}
.contact .row{display:flex;gap:12px;margin-bottom:12px}
.contact svg{flex:none;margin-top:2px}
.map{left:602px;top:2866px;width:231px;height:130px;background:linear-gradient(135deg,#eef1e8,#d9e6cf 60%,#cdd9e6)}
.foot-brand{left:930px;top:2880px;width:140px;text-align:center;font-family:"Montserrat",sans-serif;font-weight:600;font-size:14px;color:var(--white);letter-spacing:1.5px}
.social{top:2958px;width:22px;height:22px;border-radius:50%;background:var(--blue)}
.copyright{left:0;top:3058px;width:1200px;text-align:center;font-size:11px;color:#cfcfcf}
</style>
</head>
<body>

<!-- header -->
<div class="abs topbar-rule"></div>
<div class="abs topbar">
  <span>
    <svg width="11" height="11" viewBox="0 0 24 24" fill="#fff"><path d="M6.6 10.8a15.1 15.1 0 0 0 6.6 6.6l2.2-2.2c.3-.3.7-.4 1-.2 1.1.4 2.3.6 3.6.6.6 0 1 .4 1 1V20c0 .6-.4 1-1 1C10.6 21 3 13.4 3 4c0-.6.4-1 1-1h3.5c.6 0 1 .4 1 1 0 1.3.2 2.5.6 3.6.1.3 0 .7-.2 1z"/></svg>
    0064 9 404 7120</span>
  <span>
    <svg width="12" height="10" viewBox="0 0 24 18" fill="#fff"><path d="M0 0h24v2L12 10 0 2zM0 4l12 8 12-8v14H0z"/></svg>
    info@harbourlinehomes.co.nz</span>
</div>
<div class="abs brand">
  <div class="brand-mark"></div>
  <div class="brand-name">HARBOURLINE<br>HOMES</div>
</div>
<svg class="abs nav-hex" width="58" height="64" viewBox="0 0 58 64"><polygon points="29,1 57,16 57,48 29,63 1,48 1,16" fill="#f4f4f4" stroke="#e2e2e2"/></svg>
<div class="abs nav active" style="left:524px">HOME</div>
<div class="abs nav" style="left:604px">ABOUT US</div>
<div class="abs nav" style="left:713px">SERVICES</div>
<div class="abs nav" style="left:816px">RECENT PROJECTS</div>
<div class="abs nav" style="left:975px">CONTACT US</div>

<!-- hero -->
<div class="abs hero" role="img" aria-label="Photo of a smiling family sitting on the lawn in front of a stone and brick house"></div>
<div class="abs hero-arrow" style="left:81px"><svg width="44" height="44" viewBox="0 0 44 44"><path d="M25 14l-8 8 8 8" stroke="#fff" stroke-width="3" fill="none"/></svg></div>
<div class="abs hero-arrow" style="left:1075px"><svg width="44" height="44" viewBox="0 0 44 44"><path d="M19 14l8 8-8 8" stroke="#fff" stroke-width="3" fill="none"/></svg></div>
<div class="abs hero-band">We Build Residential House And Light Commercial</div>

<!-- about -->
<div class="abs heading" style="left:144px;top:640px">ABOUT <span>HARBOURLINE HOMES</span></div>
<svg class="abs" style="left:144px;top:686px" width="240" height="22" viewBox="0 0 240 22">
  <line x1="0" y1="11" x2="240" y2="11" stroke="#ddd" stroke-dasharray="2 2"/>
  <polygon points="12,1 22,6 22,16 12,21 2,16 2,6" fill="#fff" stroke="#bbb" stroke-width="1.5"/>
  <polygon points="12,6 17,9 17,14 12,17 7,14 7,9" fill="#ccc"/>
</svg>
<p class="abs about-text">Harbourline Homes is a family-run builder creating quality residential houses and light commercial spaces across Auckland. Our in-house designer shapes every interior with you, from layout and finishes to lighting and storage, so each room suits the way you live. Before any work begins on site, we model the whole project in detail, letting you and our construction team walk through the design, test ideas and settle choices early. This careful planning keeps budgets clear, timelines steady and surprises rare. From first sketch to final handover, we build homes that middle-class New Zealand families are proud to live in for years to come.</p>
<div class="btn" style="left:142px;top:907px;width:99px;height:29px">READ MORE</div>

<div class="abs estimate"></div>
<div class="abs estimate-tab">GET A FREE ESTIMATE</div>
<div class="abs field" style="top:732px;height:31px">Name</div>
<div class="abs field" style="top:769px;height:31px">Email</div>
<div class="abs field" style="top:806px;height:31px">Services
  <svg style="position:absolute;right:10px;top:12px" width="8" height="6" viewBox="0 0 8 6"><path d="M0 0h8L4 6z" fill="#666"/></svg></div>
<div class="abs field" style="top:845px;height:52px">Message</div>
<div class="btn" style="left:812px;top:907px;width:233px;height:29px">SUBMIT</div>

<!-- services -->
<div class="abs services-bg"></div>
<div class="abs heading center" style="top:1070px">OUR <span>SERVICES</span></div>
<svg class="divider" style="top:1113px" viewBox="0 0 320 26">
  <line x1="0" y1="13" x2="138" y2="13" stroke="#ccc"/><line x1="182" y1="13" x2="320" y2="13" stroke="#ccc"/>
  <polygon points="160,1 171,7 171,19 160,25 149,19 149,7" fill="#bbb"/><polygon points="160,7 165,10 165,16 160,19 155,16 155,10" fill="#eee"/>
</svg>

<div class="abs card" style="left:140px">
  <div class="card-img" role="img" aria-label="Photo of a modern two-storey white family home lit at dusk" style="background:linear-gradient(180deg,#5a7fae 0%,#8fa6c1 45%,#c9c2b0 75%,#4d5a4a 100%)"></div>
  <svg style="position:absolute;left:176px;top:172px" width="86" height="96" viewBox="0 0 86 96">
    <polygon points="43,2 84,25 84,71 43,94 2,71 2,25" fill="var(--blue)" stroke="#fff" stroke-width="3"/>
    <path d="M43 30l-20 17h6v18h10v-11h8v11h10V47h6z" fill="#fff"/>
  </svg>
  <div class="card-title">RESIDENTIAL SERVICES</div>
  <p class="card-text">Warm, practical family homes built to last, with interior design and full project modelling included so you can see every room before we break ground.</p>
  <div class="btn" style="left:169px;top:375px;width:99px;height:29px">READ MORE</div>
</div>
<div class="abs card" style="left:623px">
  <div class="card-img" role="img" aria-label="Photo of glass commercial towers against a pale blue sky" style="background:linear-gradient(180deg,#b9cfe6 0%,#d9e3ee 50%,#9fb3c8 80%,#c9d2d9 100%)"></div>
  <svg style="position:absolute;left:176px;top:172px" width="86" height="96" viewBox="0 0 86 96">
    <polygon points="43,2 84,25 84,71 43,94 2,71 2,25" fill="var(--blue)" stroke="#fff" stroke-width="3"/>
    <path d="M28 66V36l14-6v36zM44 66V40l14 4v22z" fill="#fff"/>
    <path d="M32 40h6M32 46h6M32 52h6M32 58h6M48 48h6M48 54h6M48 60h6" stroke="var(--blue)" stroke-width="2"/>
  </svg>
  <div class="card-title">COMMERCIAL SERVICES</div>
  <p class="card-text">Light commercial buildings for offices, shops and studios, planned in detail and delivered on time with clear costs and steady communication throughout.</p>
  <div class="btn" style="left:169px;top:375px;width:99px;height:29px">READ MORE</div>
</div>

<!-- recent projects -->
<div class="abs heading center" style="top:1715px">RECENT <span>PROJECTS</span></div>
<svg class="divider" style="top:1760px" viewBox="0 0 320 26">
  <line x1="0" y1="13" x2="138" y2="13" stroke="#ccc"/><line x1="182" y1="13" x2="320" y2="13" stroke="#ccc"/>
  <polygon points="160,1 171,7 171,19 160,25 149,19 149,7" fill="#bbb"/><polygon points="160,7 165,10 165,16 160,19 155,16 155,10" fill="#eee"/>
</svg>

<svg class="abs" style="left:0;top:1790px" width="1200" height="460" viewBox="0 0 1200 460">
  <defs>
    <linearGradient id="house-brick" x1="0" y1="0" x2="0" y2="1"><stop offset="0" stop-color="#7fa6d6"/><stop offset=".55" stop-color="#8a5a48"/><stop offset="1" stop-color="#4f8a34"/></linearGradient>
    <linearGradient id="tower-glass" x1="0" y1="0" x2="0" y2="1"><stop offset="0" stop-color="#3f7dd0"/><stop offset=".6" stop-color="#a9bccf"/><stop offset="1" stop-color="#6e7e8c"/></linearGradient>
    <linearGradient id="house-dusk" x1="0" y1="0" x2="0" y2="1"><stop offset="0" stop-color="#4a78c2"/><stop offset=".55" stop-color="#7d8594"/><stop offset="1" stop-color="#4c6b3a"/></linearGradient>
    <linearGradient id="office-blue" x1="0" y1="0" x2="0" y2="1"><stop offset="0" stop-color="#5d95de"/><stop offset=".6" stop-color="#2f5f9d"/><stop offset="1" stop-color="#8fa0b0"/></linearGradient>
    <linearGradient id="office-white" x1="0" y1="0" x2="0" y2="1"><stop offset="0" stop-color="#2a62c4"/><stop offset=".5" stop-color="#e4e8ee"/><stop offset="1" stop-color="#9aa3ad"/></linearGradient>
    <linearGradient id="house-lawn" x1="0" y1="0" x2="0" y2="1"><stop offset="0" stop-color="#6aa2e0"/><stop offset=".55" stop-color="#c8ae85"/><stop offset="1" stop-color="#5f9a34"/></linearGradient>
  </defs>
  <g stroke="var(--blue)" stroke-width="4">
    <polygon role="img" aria-label="Photo of a brick two-storey family house" points="243,10 346,69 346,187 243,246 140,187 140,69" fill="url(#house-brick)"/>
    <polygon role="img" aria-label="Photo of modern glass office towers" points="480,10 583,69 583,187 480,246 377,187 377,69" fill="url(#tower-glass)"/>
    <polygon role="img" aria-label="Photo of a suburban house with garage at dusk" points="717,10 820,69 820,187 717,246 614,187 614,69" fill="url(#house-dusk)"/>
    <polygon role="img" aria-label="Photo of a blue glass commercial building" points="955,10 1058,69 1058,187 955,246 852,187 852,69" fill="url(#office-blue)"/>
    <polygon role="img" aria-label="Photo of a white modern office block" points="363,220 466,279 466,397 363,456 260,397 260,279" fill="url(#office-white)"/>
    <polygon role="img" aria-label="Photo of a family house with a green lawn" points="837,220 940,279 940,397 837,456 734,397 734,279" fill="url(#house-lawn)"/>
  </g>
  <polygon points="600,214 706,275 706,397 600,458 494,397 494,275" fill="var(--blue)"/>
  <text x="600" y="332" text-anchor="middle" font-family="Montserrat, sans-serif" font-weight="600" font-size="17" fill="#fff" letter-spacing="1.5">HARBOURLINE</text>
  <text x="600" y="354" text-anchor="middle" font-family="Montserrat, sans-serif" font-weight="600" font-size="17" fill="#fff" letter-spacing="1.5">HOMES</text>
</svg>

<!-- testimonials -->
<div class="abs testi-bg"></div>
<div class="abs heading center" style="top:2363px">CLIENT <span>TESTIMONIALS</span></div>
<svg class="divider" style="top:2408px" viewBox="0 0 320 26">
  <line x1="0" y1="13" x2="138" y2="13" stroke="#ccc"/><line x1="182" y1="13" x2="320" y2="13" stroke="#ccc"/>
  <polygon points="160,1 171,7 171,19 160,25 149,19 149,7" fill="#bbb"/><polygon points="160,7 165,10 165,16 160,19 155,16 155,10" fill="#eee"/>
</svg>
<svg class="abs" style="left:254px;top:2494px" width="14" height="24" viewBox="0 0 14 24"><path d="M12 2L2 12l10 10" stroke="#bbb" stroke-width="2" fill="none"/></svg>
<svg class="abs" style="left:928px;top:2494px" width="14" height="24" viewBox="0 0 14 24"><path d="M2 2l10 10L2 22" stroke="#bbb" stroke-width="2" fill="none"/></svg>
<div class="abs avatar active" style="left:303px" role="img" aria-label="Portrait of client Daniel Hart"></div>
<div class="abs avatar" style="left:475px" role="img" aria-label="Portrait of client Leah Moreno"></div>
<div class="abs avatar" style="left:635px" role="img" aria-label="Portrait of client Sam Porter"></div>
<div class="abs avatar" style="left:807px" role="img" aria-label="Portrait of client Owen Clarke"></div>
<div class="abs person active" style="left:268px">Daniel Hart</div>
<div class="abs person" style="left:440px">Leah Moreno</div>
<div class="abs person" style="left:600px">Sam Porter</div>
<div class="abs person" style="left:772px">Owen Clarke</div>
<svg class="abs" style="left:335px;top:2596px" width="26" height="13" viewBox="0 0 26 13"><path d="M0 13L13 0l13 13z" fill="#fff" stroke="#d8d8d8"/><path d="M1 13h24" stroke="#fff" stroke-width="2"/></svg>
<div class="abs quote">
  <span class="quote-mark" style="position:absolute;left:20px;top:10px">&ldquo;</span>
  Seeing a full model of our house before the first post went in made every decision easier. The team listened, kept us updated each week and finished on budget. Our new home feels exactly as we imagined it, and the interior design advice was a real bonus for the whole family.
  <span class="quote-mark" style="position:absolute;right:20px;bottom:-6px">&rdquo;</span>
</div>

<!-- footer -->
<div class="abs footer" role="img" aria-label="Dim photo of a city skyline at night behind the footer"></div>
<div class="abs foot-head" style="left:144px">QUICK LINKS</div>
<div class="abs foot-head" style="left:355px">CONTACT DETAILS</div>
<div class="abs foot-head" style="left:602px">LOCATION MAP</div>
<ul class="abs foot-links">
  <li>Home</li><li>About Us</li><li>Services</li><li>Recent Projects</li><li>Contact Us</li>
</ul>
<div class="abs contact">
  <div class="row">
    <svg width="12" height="16" viewBox="0 0 12 16"><path d="M6 0a6 6 0 0 0-6 6c0 4.5 6 10 6 10s6-5.5 6-10a6 6 0 0 0-6-6zm0 8.5a2.5 2.5 0 1 1 0-5 2.5 2.5 0 0 1 0 5z" fill="#fff"/></svg>
    <div>HARBOURLINE HOMES<br>18 Kestrel Rise,<br>Eastfield Auckland</div>
  </div>
  <div class="row">
    <svg width="13" height="13" viewBox="0 0 24 24" fill="#fff"><path d="M6.6 10.8a15.1 15.1 0 0 0 6.6 6.6l2.2-2.2c.3-.3.7-.4 1-.2 1.1.4 2.3.6 3.6.6.6 0 1 .4 1 1V20c0 .6-.4 1-1 1C10.6 21 3 13.4 3 4c0-.6.4-1 1-1h3.5c.6 0 1 .4 1 1 0 1.3.2 2.5.6 3.6.1.3 0 .7-.2 1z"/></svg>
    <div>0064 9 404 7120</div>
  </div>
  <div class="row">
    <svg width="13" height="13" viewBox="0 0 24 24" fill="#fff"><path d="M6 2h12v6H6zM3 9h18v9h-3v4H6v-4H3zm5 6v5h8v-5z"/></svg>
    <div>0064 9 404 7120</div>
  </div>
  <div class="row">
    <svg width="13" height="13" viewBox="0 0 24 24"><circle cx="12" cy="12" r="10" fill="none" stroke="#fff" stroke-width="2"/><circle cx="12" cy="12" r="4" fill="none" stroke="#fff" stroke-width="2"/></svg>
    <div>info@harbourlinehomes.co.nz</div>
  </div>
</div>
<div class="abs map" role="img" aria-label="Street map showing the office location with a red pin"></div>
<div class="abs foot-brand">HARBOURLINE<br>HOMES</div>
<div class="abs social" style="left:944px"></div>
<div class="abs social" style="left:972px"></div>
<div class="abs social" style="left:1000px"></div>
<div class="abs social" style="left:1028px;background:#d23b2f"></div>
<div class="abs copyright">Copyright © 2017 HARBOURLINE HOMES. All Rights Reserved.</div>

</body>
</html>
```